Makeup Artist Requires Business Card design

Hi

I am looking for a business card design to market my makeup artist business. I operate under my own name Mara Veldt and I would like to keep the design of the card very simplistic and chic - something that keeps both my name and profession (makeup artist) the focus of the card. I would like it to be a style that is eyecatching to the reader (i am open to anything unusual) but upmarket.

Target Market(s)

women, magazine/beauty/fashion editors, photographers.

Industry/Entity Type

Business

Requirements
Must have
• Must contain:

Phone number: 0418 372 915
Website: www.maraveldt.com.au
email: contact@maraveldt.com.au

(although you don't need to have prefaced these with the words phone number, website etc :))
Should not have
• I am not looking for anything overly colorful - my preference is to keep the card dark if possible.

```html
<!DOCTYPE html>
<html lang="en">
<head>
<meta charset="utf-8">
<title>Mara Veldt – Makeup Artist Business Card</title>
<link rel="stylesheet" href="https://fonts.googleapis.com/css2?family=Quicksand:wght@400;500;700&display=swap">
<style>
  :root {
    --backdrop: #2b2b2b;
    --card: #151515;
    --name: #b9b9b9;
    --role: #9c9c9c;
    --contact: #c4c4c4;
    --icon: #a8a8a8;
  }
  * { margin: 0; padding: 0; box-sizing: border-box; }
  html, body {
    width: 1200px;
    height: 1000px;
    overflow: hidden;
    background: var(--backdrop);
    font-family: "Quicksand", sans-serif;
  }
  .canvas { position: relative; width: 1200px; height: 1000px; }

  .card {
    position: absolute;
    left: 250px;
    width: 686px;
    height: 391px;
    background: var(--card);
    box-shadow: 0 6px 18px rgba(0,0,0,0.45);
  }
  .card--front { top: 84px; }
  .card--back { top: 528px; }

  .wordmark { position: absolute; left: 146px; top: 160px; width: 400px; }
  .wordmark__name {
    display: block;
    font-weight: 500;
    font-size: 48px;
    line-height: 56px;
    color: var(--name);
    letter-spacing: 1px;
  }
  .wordmark__role {
    display: block;
    margin-left: 157px;
    font-weight: 500;
    font-size: 17px;
    letter-spacing: 2.6px;
    color: var(--role);
    line-height: 20px;
  }

  .contact-list {
    position: absolute;
    left: 412px;
    top: 276px;
    list-style: none;
  }
  .contact-list__item {
    display: flex;
    align-items: center;
    height: 27px;
    font-size: 13px;
    color: var(--contact);
    letter-spacing: 0.3px;
  }
  .contact-list__icon { width: 20px; height: 16px; margin-right: 10px; fill: none; stroke: var(--icon); stroke-width: 1.4; }

  .contact-block {
    position: absolute;
    top: 324px;
    font-size: 13px;
    color: var(--contact);
    line-height: 17px;
    letter-spacing: 0.3px;
  }
  .contact-block__label { display: block; font-weight: 700; }
  .contact-block--phone { left: 80px; top: 326px; }
  .contact-block--web { left: 235px; }
  .contact-block--email { left: 469px; }
</style>
</head>
<body>
<div class="canvas">

  <section class="card card--front" aria-label="Card front">
    <div class="wordmark">
      <span class="wordmark__name">Mara Veldt</span>
      <span class="wordmark__role">MAKEUP ARTIST</span>
    </div>
    <ul class="contact-list">
      <li class="contact-list__item">
        <svg class="contact-list__icon" viewBox="0 0 20 16" aria-hidden="true">
          <path d="M2 6 Q10 0 18 6 L16 8 L13 6 L7 6 L4 8 Z" fill="#a8a8a8"/>
          <rect x="5" y="8" width="10" height="6" rx="1" fill="#a8a8a8"/>
        </svg>
        0418 372 915
      </li>
      <li class="contact-list__item">
        <svg class="contact-list__icon" viewBox="0 0 20 16" aria-hidden="true">
          <circle cx="10" cy="8" r="7"/>
          <ellipse cx="10" cy="8" rx="3" ry="7"/>
          <path d="M3 8 H17 M4.5 4.5 H15.5 M4.5 11.5 H15.5"/>
        </svg>
        www.maraveldt.com.au
      </li>
      <li class="contact-list__item">
        <svg class="contact-list__icon" viewBox="0 0 20 16" aria-hidden="true">
          <rect x="2" y="3.5" width="16" height="10"/>
          <path d="M2 3.5 L10 9.5 L18 3.5"/>
        </svg>
        contact@maraveldt.com.au
      </li>
    </ul>
  </section>

  <section class="card card--back" aria-label="Card back">
    <div class="wordmark">
      <span class="wordmark__name">Mara Veldt</span>
      <span class="wordmark__role">MAKEUP ARTIST</span>
    </div>
    <div class="contact-block contact-block--phone">
      <span class="contact-block__label">Phone:</span>
      0418 372 915
    </div>
    <div class="contact-block contact-block--web">
      <span class="contact-block__label">Web:</span>
      www.maraveldt.com.au
    </div>
    <div class="contact-block contact-block--email">
      <span class="contact-block__label">Email:</span>
      contact@maraveldt.com.au
    </div>
  </section>

</div>
</body>
</html>
```